Aircraft Spares Supplier
Stationary/Business Cards
Project: Aircraft Spares Supplier
Aircraft Spares Supplier  - Aviation
Creative Brief
Use standard fonts
I am flexible on the font
Rowan Pettibone
Managing Director
PO Box 71829 Dubai United Arab Emirates
UAE Toll Free 800 KLIM
TBA
rowan@velmoro-skyparts.com
www.velmoro.example
We will be moving to a new address with new numbers in the next few months, I would like to get the format prepared that will apply to multiple address' Card size European 9cm x 5.5cm

```html
<!DOCTYPE html>
<html lang="en">
<head>
<meta charset="utf-8">
<title>Velmoro Stationery</title>
<link href="https://fonts.googleapis.com/css2?family=Open+Sans:wght@400;800&display=swap" rel="stylesheet">
<style>
:root{
  --bg:#4b3426;
  --paper:#ffffff;
  --blue:#2e8fd8;
  --blue-light:#8fc6ec;
  --grey:#7c7e82;
  --grey-dark:#5d5f63;
  --grey-light:#c9cbce;
  --ink:#4a4d52;
  --label:#d8cfc6;
}
*{margin:0;padding:0;box-sizing:border-box}
html,body{width:1200px;height:466px;overflow:hidden}
body{background:var(--bg);font-family:"Open Sans",Arial,sans-serif;position:relative;color:var(--ink)}
.sheet{position:absolute;background:var(--paper);box-shadow:0 2px 6px rgba(0,0,0,.4);overflow:hidden}
.sheet svg.waves{position:absolute;left:0;bottom:0;width:100%;display:block}
.brand{position:absolute;display:flex;align-items:center;gap:3px;font-weight:800;color:var(--blue);white-space:nowrap}
.brand .dot{border-radius:50%;background:var(--blue);flex:none}
.label{position:absolute;font-size:4.5px;letter-spacing:.16em;color:var(--label);text-transform:uppercase;text-align:center;white-space:nowrap}
.contact{position:absolute;font-size:3px;line-height:4px;color:var(--ink);white-space:nowrap}
.footer-line{position:absolute;left:0;right:0;text-align:center;font-size:3px;color:var(--ink);white-space:nowrap}

/* cards */
.card{width:80px;height:49px;left:29px}
.card-front{top:170px}
.card-front .brand{left:6px;top:6px;font-size:6px}
.card-front .brand .dot{width:5px;height:5px}
.card-front .contact{left:6px;top:17px;font-size:2.6px;line-height:3.4px}
.card-back{top:246px}
.card-back .brand{left:50%;top:50%;transform:translate(-50%,-50%);font-size:7px}
.card-back .brand .dot{width:6px;height:6px}

/* letterheads */
.letterhead{top:36px;width:264px;height:360px}
.letterhead-one{left:187px}
.letterhead-two{left:473px}
.letterhead .brand{left:20px;top:18px;font-size:9px}
.letterhead .brand .dot{width:8px;height:8px}
.letterhead .contact{left:200px;top:16px}
.letterhead-two .footer-line{bottom:22px}

/* envelopes */
.envelope-back{left:828px;top:96px;width:348px;height:168px;background:#f1f2f4}
.envelope-back .brand{left:50%;top:92px;transform:translateX(-50%);font-size:6px}
.envelope-back .brand .dot{width:5px;height:5px}
.envelope-front{left:773px;top:262px;width:403px;height:134px}
.envelope-front .brand{left:22px;top:64px;font-size:7px}
.envelope-front .brand .dot{width:6px;height:6px}
</style>
</head>
<body>

<div class="label" style="left:19px;top:146px;width:100px">Stationery Concepts</div>
<section class="sheet card card-front" aria-label="Business card front">
  <div class="brand"><span class="dot"></span>VELMORO</div>
  <div class="contact">Rowan Pettibone<br>Managing Director<br>PO Box 71829<br>800 KLIM<br>rowan@velmoro-skyparts.com</div>
</section>
<div class="label" style="left:19px;top:224px;width:100px">Business Card Front</div>
<section class="sheet card card-back" aria-label="Business card back">
  <div class="brand"><span class="dot"></span>VELMORO</div>
</section>
<div class="label" style="left:19px;top:300px;width:100px">Business Card Back</div>

<section class="sheet letterhead letterhead-one" aria-label="Letterhead option 1">
  <div class="brand"><span class="dot"></span>VELMORO</div>
  <div class="contact">PO Box 71829<br>800 KLIM<br>rowan@velmoro-skyparts.com<br>www.velmoro.example</div>
  <svg class="waves" viewBox="0 0 264 40" preserveAspectRatio="none" height="40">
    <path d="M0 10 Q130 34 264 6 V16 Q130 40 0 20Z" fill="var(--grey)"/>
    <path d="M0 24 Q130 40 264 16 V40 H0Z" fill="var(--blue)"/>
    <path d="M0 26 Q130 38 264 20 V23 Q130 42 0 30Z" fill="var(--blue-light)"/>
  </svg>
</section>
<section class="sheet letterhead letterhead-two" aria-label="Letterhead option 2">
  <div class="brand"><span class="dot"></span>VELMORO</div>
  <div class="contact">PO Box 71829<br>800 KLIM<br>rowan@velmoro-skyparts.com<br>www.velmoro.example</div>
  <div class="footer-line">PO Box 71829 · 800 KLIM · rowan@velmoro-skyparts.com · www.velmoro.example</div>
  <svg class="waves" viewBox="0 0 264 22" preserveAspectRatio="none" height="22">
    <path d="M0 6 Q130 22 264 2 V8 Q130 26 0 12Z" fill="var(--grey-light)"/>
    <path d="M0 14 Q130 24 264 8 V22 H0Z" fill="var(--blue)"/>
  </svg>
</section>
<div class="label" style="left:187px;top:404px;width:264px">Letter Head Option 1</div>
<div class="label" style="left:473px;top:404px;width:264px">Letter Head Option 2</div>

<section class="sheet envelope-back" aria-label="Envelope back">
  <svg viewBox="0 0 348 168" preserveAspectRatio="none" width="348" height="168" style="position:absolute;left:0;top:0">
    <path d="M0 0 H348 V62 Q174 86 0 62Z" fill="var(--grey)"/>
    <path d="M0 0 H348 V52 Q174 74 0 52Z" fill="var(--grey-dark)"/>
    <path d="M0 110 L110 104 L0 168Z M348 110 L238 104 L348 168Z" fill="#e4e6e9"/>
  </svg>
  <div class="brand"><span class="dot"></span>VELMORO</div>
</section>
<section class="sheet envelope-front" aria-label="Envelope front">
  <div class="brand"><span class="dot"></span>VELMORO</div>
  <svg class="waves" viewBox="0 0 403 30" preserveAspectRatio="none" height="30">
    <path d="M0 8 Q200 28 403 4 V12 Q200 32 0 14Z" fill="var(--grey)"/>
    <path d="M0 18 Q200 32 403 12 V30 H0Z" fill="var(--blue)"/>
  </svg>
</section>
<div class="label" style="left:773px;top:404px;width:403px">Envelope Option 2</div>

</body>
</html>
```